Tech Savy small Business accountant business card design

We need a business card for a new company based in the cloud. We provide tax, business advisory, accounting, information technology solutions and back office functions to small businesses. We offer fixed fee packages with add on services as you need them. By harnessing technology we simplify small business operational processes providing valuable time and information for small business owners to grow their business. In the logo (zulvarine) we want to be able to see zulv and experts. The final design should communicate achieving growth dreams and balance (ie life and $).
Updates
This project has been temporarily placed on hold until I finalize "Tech Savy small Business accountant needs a logo". I invite all designers to submit on this logo project. Once my logo is finalized I will resume this business card contest. Thanks Added Wednesday, March 19, 2014
This project has been temporarily placed on hold until I finalize "Tech Savy small Business accountant logo". I invite all designers to submit on this logo project. Once my logo is finalized I will resume this business card contest. Thanks Added Thursday, March 20, 2014
Target Market(s)
Small Business (Revenue $500,000, more than 3 employees) owners.
Industry/Entity Type
Small Business
Contact Information for Business Card
Marla Pennick (Principal)
Accountant, Tax Agent.
TEL | 0417 583 916
EMAIL | Marla.Pennick@zulvarine.com.au
WEB | www.zulvarine.com.au
Look and feel

```html
<!DOCTYPE html>
<html lang="en">
<head>
<meta charset="utf-8">
<title>zulvarine — business card</title>
<link rel="stylesheet" href="https://fonts.googleapis.com/css2?family=Roboto+Condensed:wght@300;700&display=swap">
<style>
  :root {
    --ink-black: #000000;
    --shade-grey: #2a2d30;
    --band-gold: #c49a0e;
    --band-gold-deep: #b58c08;
    --logo-slate: #353a3e;
    --accent-blue: #0b40c4;
    --tagline-white: #f2f2f2;
  }
  html, body {
    margin: 0;
    padding: 0;
    width: 1200px;
    height: 720px;
    overflow: hidden;
    background: var(--ink-black);
  }
  .card {
    display: block;
    width: 1200px;
    height: 720px;
  }
  .brand-name {
    font-family: "Roboto Condensed", "Arial Narrow", sans-serif;
    font-weight: 700;
    font-size: 188px;
    letter-spacing: -2px;
    fill: var(--logo-slate);
  }
  .brand-square {
    fill: var(--accent-blue);
  }
  .tagline {
    font-family: "Roboto Condensed", "Arial Narrow", sans-serif;
    font-weight: 300;
    font-size: 29px;
    letter-spacing: 4.4px;
    fill: var(--tagline-white);
  }
</style>
</head>
<body>
<svg class="card" viewBox="0 0 1200 720" xmlns="http://www.w3.org/2000/svg">
  <defs>
    <linearGradient id="leftShade" x1="0" y1="0" x2="1" y2="0">
      <stop offset="0" stop-color="var(--ink-black)"/>
      <stop offset="1" stop-color="var(--shade-grey)"/>
    </linearGradient>
    <linearGradient id="rightShade" x1="0" y1="0" x2="1" y2="0">
      <stop offset="0" stop-color="var(--shade-grey)"/>
      <stop offset="0.55" stop-color="var(--ink-black)"/>
    </linearGradient>
    <linearGradient id="bandFill" x1="0" y1="0" x2="1" y2="1">
      <stop offset="0" stop-color="var(--band-gold)"/>
      <stop offset="1" stop-color="var(--band-gold-deep)"/>
    </linearGradient>
  </defs>

  <rect class="backdrop" x="0" y="0" width="1200" height="720" fill="var(--ink-black)"/>

  <g class="side-panel side-panel-left" role="img" aria-label="Dark side panel with a scattered pattern of soft grey bubbles">
    <polygon points="0,0 53,0 411,720 0,720" fill="url(#leftShade)"/>
  </g>
  <g class="side-panel side-panel-right" role="img" aria-label="Dark side panel with a scattered pattern of soft grey bubbles">
    <polygon points="837,0 1200,0 1200,720 1189,720" fill="url(#rightShade)"/>
  </g>

  <polygon class="gold-band" points="53,0 837,0 1189,720 411,720" fill="url(#bandFill)"/>

  <g class="brand-lockup">
    <text class="brand-name" x="245" y="405">zulvarine</text>
    <rect class="brand-square" x="921" y="349" width="56" height="56"/>
  </g>
  <text class="tagline" x="626" y="472" text-anchor="middle">YOUR BUSINESS AND ACCOUNTING PARTNER</text>
</svg>
</body>
</html>
```